Business Card for Childrens Book Publisher

Would like a business card that reflects a newly established boutique childrens publishing company. The first project is a book to help raise children's self esteem titled "The Brave Little Fern." To get a better idea of the type of look I am after go to te website www.bravelittlefern.com.au. You can take the images from the book and use them for the business card. Would like it to have a fun innovative look and feel to it. The business is about being uplifting and positive for children, but also creating beautiful, high quality books. You can use whatever images you see on the website but I have more high res files that I can send to you over drop box or some other programs if you need them.I would like the business card to be two sided.

The information on the business card is:

Marigold Lantern Books
Helena Marsk
Publisher/Author

Marigold Lantern Books
little lanterns glowing bright
T 0491 356 207
Po Box 64, Kellerton, Vic 3195, Australia
ABN: 36 507 619 824
helenamarsk@marigoldlanternbooks.com
www.marigoldlanternbooks.com

Target Market(s)

Booksellers, parents, schools, kindergartens, owners of children's boutiques, retailers.

Industry/Entity Type

Boutique

Requirements
Must have
• Would it to be double sided.

```html
<!DOCTYPE html>
<html lang="en">
<head>
<meta charset="utf-8">
<title>Marigold Lantern Books – Business Card</title>
<link rel="stylesheet" href="https://fonts.googleapis.com/css2?family=Gochi+Hand&display=swap">
<style>
  :root {
    --backdrop-dark: #3f3f3f;
    --backdrop-light: #5e5e5e;
    --card: #ffffff;
    --ink: #6a4a38;
    --art-sky: #e9eef2;
    --art-blue: #5f7fb8;
    --art-yellow: #f2c94c;
    --art-green: #7fae5a;
    --art-earth: #c8a77a;
  }
  * { margin: 0; padding: 0; box-sizing: border-box; }
  html, body { width: 1200px; height: 900px; overflow: hidden; }
  body {
    position: relative;
    background: radial-gradient(ellipse at center, var(--backdrop-light), var(--backdrop-dark));
    font-family: "Gochi Hand", cursive;
    color: var(--ink);
  }
  .card {
    position: absolute;
    top: 44px;
    height: 778px;
    background: var(--card);
    box-shadow: 0 6px 18px rgba(0,0,0,0.35);
    text-align: center;
  }
  .card--front { left: 92px; width: 446px; }
  .card--back { left: 606px; width: 502px; }

  .front__title {
    position: absolute; top: 84px; left: 0; right: 0;
    font-size: 52px; line-height: 60px;
  }
  .front__art {
    position: absolute; top: 262px; left: 104px; width: 190px; height: 336px;
    border-radius: 40px 40px 12px 12px;
    background: linear-gradient(180deg, #e8c7a6 0%, var(--art-yellow) 35%, var(--art-blue) 70%, #f1f1f1 100%);
    opacity: 0.85;
  }
  .front__name {
    position: absolute; top: 660px; left: 0; right: 0;
    font-size: 40px;
  }
  .front__role {
    position: absolute; top: 712px; left: 0; right: 0;
    font-size: 17px;
  }

  .back__tagline {
    position: absolute; top: 70px; left: 0; right: 0;
    font-size: 36px; line-height: 44px;
  }
  .back__art {
    position: absolute; top: 172px; left: 34px; width: 432px; height: 214px;
    border-radius: 50% 50% 12px 12px / 30% 30% 12px 12px;
    background: linear-gradient(180deg, var(--art-sky) 0%, var(--art-yellow) 35%, var(--art-green) 62%, var(--art-earth) 100%);
    opacity: 0.85;
  }
  .back__name {
    position: absolute; top: 470px; left: 0; right: 0;
    font-size: 48px;
  }
  .back__contact {
    position: absolute; top: 560px; left: 0; right: 0;
    list-style: none;
    font-size: 22px; line-height: 32px;
  }
  .back__web {
    position: absolute; top: 716px; left: 0; right: 0;
    font-size: 30px;
  }
</style>
</head>
<body>
  <section class="card card--front">
    <h1 class="front__title">Marigold Lantern<br>Books</h1>
    <div class="front__art" role="img" aria-label="Illustration of a small child with a blue school backpack looking upward"></div>
    <p class="front__name">- Helena Marsk -</p>
    <p class="front__role">Publisher / Author</p>
  </section>

  <section class="card card--back">
    <p class="back__tagline">little lanterns<br>glowing bright</p>
    <div class="back__art" role="img" aria-label="Illustration of two children in raincoats splashing in a puddle"></div>
    <h2 class="back__name">Helena Marsk</h2>
    <ul class="back__contact">
      <li>T 0491 356 207</li>
      <li>Po Box 64, Kellerton, Vic 3195, Australia</li>
      <li>ABN: 36 507 619 824</li>
      <li>helenamarsk@marigoldlanternbooks.com</li>
    </ul>
    <p class="back__web">www.marigoldlanternbooks.com</p>
  </section>
</body>
</html>
```